Menu Re-Design for The Marlowbrook a british eatery in spanish holiday resort

Looking for a new design for our breakfast and lunch menu....

I have included some pictures of a few menus I like the feel of File No 1,2,3,4,5..... but am open to any ideas you may have....

The menu is to be double sided consisting of a front design with actual menu on reverse....

I have also included the relevant text files you will require...

We do not have a logo or set colour scheme to follow...

Target Market(s)

Predominantly British holidaymakers in popular Spanish resort....

Requirements
Must have
• Menu to be A3 and double sided, split between either a front page design and menu on reverse, or menu divided between both sides....
• Company Name:- The Marlowbrook
Nice to have
• Fun and Bold design whilst maintaining a feel of quality....
Should not have
• Please avoid the use of any food photography....

```html
<!DOCTYPE html>
<html lang="en">
<head>
<meta charset="utf-8">
<title>The Marlowbrook – Daytime Menu</title>
<link href="https://fonts.googleapis.com/css2?family=Open+Sans:ital,wght@0,600;0,700;1,400&family=Sail&display=swap" rel="stylesheet">
<style>
  :root{
    --brown:#5a3214;
    --band:#5c3717;
    --band-edge:#7b7b7b;
    --paper:#f3f3f3;
    --ribbon:#d9262c;
    --gold:#fdbc16;
    --art:#e9e2da;
    --art-deep:#ddd1c4;
  }
  *{margin:0;padding:0;box-sizing:border-box}
  html,body{width:1200px;height:848px;overflow:hidden;background:var(--paper)}
  .menu{position:relative;width:1200px;height:848px;background:var(--paper);color:var(--brown);
    font-family:"Open Sans",Arial,sans-serif;font-weight:700;font-size:13px}
  .top-band{position:absolute;left:0;top:0;width:1200px;height:68px;background:var(--band);border-bottom:5px solid var(--band-edge)}
  .brand{position:absolute;left:460px;top:82px;width:280px;height:70px;display:flex;align-items:center;justify-content:center;gap:12px}
  .brand-dot{width:26px;height:26px;border-radius:50%;background:var(--gold);flex:none}
  .brand-name{font-family:"Sail",cursive;font-weight:400;font-size:38px;color:var(--brown);white-space:nowrap}
  .ribbon{position:absolute;left:930px;top:38px;width:195px;height:34px;background:var(--ribbon);color:#fff;
    font-weight:600;font-size:22px;line-height:34px;text-align:center}
  .ribbon::before,.ribbon::after{content:"";position:absolute;top:4px;width:14px;height:26px;background:#a81b20}
  .ribbon::before{left:-14px}
  .ribbon::after{right:-14px}
  .served{position:absolute;left:948px;top:74px;font-weight:600;font-size:20px;color:#222}
  .heading{position:absolute;font-family:"Sail",cursive;font-weight:400;font-size:32px;line-height:1;color:var(--brown)}
  .heading::after{content:"";position:absolute;left:var(--ul-left,0);width:var(--ul-width,110px);bottom:-9px;border-bottom:1px solid var(--brown)}
  .note{position:absolute;font-style:italic;font-weight:400;font-size:11px;line-height:1.5;color:#333}
  .row{position:absolute;display:flex;justify-content:space-between;line-height:16px}
  .row small{display:block;font-weight:600;font-size:10.5px}
  .art{position:absolute;border-radius:40%;background:radial-gradient(circle at 45% 45%,var(--art),var(--art-deep))}
</style>
</head>
<body>
<main class="menu">
  <div class="top-band"></div>
  <div class="brand"><span class="brand-dot"></span><span class="brand-name">The Marlowbrook</span></div>
  <div class="ribbon">Daytime menu</div>
  <div class="served">Served until 5pm</div>

  <!-- Wraps -->
  <h2 class="heading" style="left:35px;top:110px;--ul-left:85px;--ul-width:110px">Wraps</h2>
  <p class="note" style="left:24px;top:153px;width:300px">Chicken Breast sautéd with red pepper and onion with crisp lettuce in a Tortilla Wrap</p>
  <div class="row" style="left:22px;top:205px;width:244px">BBQ<span>6.50</span></div>
  <div class="row" style="left:22px;top:226px;width:244px">Cajun<span>6.50</span></div>
  <div class="row" style="left:22px;top:247px;width:244px">Tikka<span>6.50</span></div>
  <div class="row" style="left:22px;top:268px;width:244px">Sweet Chilli<span>6.50</span></div>
  <div class="row" style="left:22px;top:289px;width:244px">Garlic<span>6.50</span></div>
  <div class="row" style="left:22px;top:310px;width:244px">add Homemade Chips<span>2.00</span></div>
  <div class="art" role="img" aria-label="Line illustration of a filled tortilla wrap" style="left:292px;top:180px;width:172px;height:168px"></div>

  <!-- Salads -->
  <h2 class="heading" style="left:238px;top:365px;--ul-left:-35px;--ul-width:135px">Salads</h2>
  <div class="row" style="left:20px;top:415px;width:362px">Creamy Goats Cheese with Pedro Ximenez Glaze<span>7.00</span></div>
  <div class="row" style="left:20px;top:445px;width:362px">Classic Chicken Caesar &amp; Parmesan Shavings<span>7.00</span></div>
  <div class="row" style="left:20px;top:473px;width:362px">Marlowbrook Mixed Salad with House Dressing<span>6.50</span></div>

  <!-- Baguettes -->
  <h2 class="heading" style="left:20px;top:528px;--ul-left:0;--ul-width:0">Fresh Baked Baguettes</h2>
  <p class="note" style="left:55px;top:575px">served with homemade hand-cut chips, salad and coleslaw</p>
  <div class="row" style="left:153px;top:601px;width:225px">Tuna Cheese Melt<span>7.50</span></div>
  <div class="row" style="left:153px;top:627px;width:225px"><span>Hunters Chicken<small>(chicken, bacon, bbq sauce, melted cheese)</small></span><span>7.50</span></div>
  <div class="row" style="left:153px;top:670px;width:225px">BLT<span>7.50</span></div>
  <div class="row" style="left:153px;top:692px;width:225px">Chicken Tikka in Minted Mayo<span>7.50</span></div>
  <div class="row" style="left:153px;top:721px;width:225px;align-items:flex-end"><span>Pork &amp; Herb Sausage with<br>Fried Onion</span><span>7.50</span></div>
  <div class="row" style="left:153px;top:766px;width:225px">Chicken &amp; Bacon Mayo<span>7.50</span></div>
  <div class="art" role="img" aria-label="Line illustration of a tomato" style="left:0;top:595px;width:150px;height:195px"></div>

  <!-- Jacket Potatoes -->
  <h2 class="heading" style="left:485px;top:213px;--ul-left:10px;--ul-width:140px">Jacket Potatoes</h2>
  <p class="note" style="left:485px;top:257px">served with salad garnish and homemade coleslaw</p>
  <div class="row" style="left:491px;top:285px;width:186px">Plain<span>4.50</span></div>
  <div class="row" style="left:491px;top:307px;width:186px">Baked Beans<span>5.50</span></div>
  <div class="row" style="left:491px;top:331px;width:186px">Cheddar Cheese<span>5.50</span></div>
  <div class="row" style="left:491px;top:355px;width:186px">Tuna Mayonnaise<span>5.50</span></div>
  <div class="row" style="left:491px;top:379px;width:186px">Curry Sauce<span>5.50</span></div>
  <div class="row" style="left:491px;top:401px;width:186px">Beans &amp; Cheese<span>6.00</span></div>
  <div class="row" style="left:491px;top:425px;width:186px">Chicken Curry<span>6.50</span></div>
  <div class="row" style="left:491px;top:450px;width:186px">Chilli<span>6.50</span></div>

  <!-- Omelettes -->
  <h2 class="heading" style="left:411px;top:480px;--ul-left:10px;--ul-width:110px">Omelettes</h2>
  <p class="note" style="left:410px;top:525px">served with salad garnish and homemade coleslaw</p>
  <div class="row" style="left:450px;top:544px">Add homemade chips 2.00</div>
  <div class="row" style="left:409px;top:573px;width:220px">Plain<span>5.00</span></div>
  <div class="row" style="left:409px;top:595px;width:220px">Cheddar Cheese<span>5.50</span></div>
  <div class="row" style="left:409px;top:621px;width:220px">Ham<span>5.50</span></div>
  <div class="row" style="left:409px;top:645px;width:220px">Mushroom<span>5.50</span></div>
  <div class="row" style="left:409px;top:671px;width:220px">Cheese &amp; Onion<span>6.00</span></div>
  <div class="row" style="left:409px;top:696px;width:220px">Cheese &amp; Ham<span>6.00</span></div>
  <div class="row" style="left:409px;top:720px;width:220px">Bacon<span>6.00</span></div>
  <div class="row" style="left:409px;top:741px;width:220px">Bacon &amp; Cheese<span>6.50</span></div>
  <div class="art" role="img" aria-label="Line illustration of a mushroom" style="left:662px;top:552px;width:135px;height:150px"></div>
  <div class="art" role="img" aria-label="Line illustration of a small mushroom" style="left:656px;top:708px;width:95px;height:98px"></div>

  <!-- Lite Bites & Sides -->
  <h2 class="heading" style="left:932px;top:110px;--ul-left:35px;--ul-width:150px">Lite Bites &amp; Sides</h2>
  <div class="row" style="left:802px;top:159px;width:322px">Basket of Homemade Chips<span>3.50</span></div>
  <div class="row" style="left:802px;top:184px;width:322px">Basket of Spicy Wedges<span>3.50</span></div>
  <div class="row" style="left:802px;top:211px;width:322px">Basket of Onion Rings<span>3.50</span></div>
  <div class="row" style="left:802px;top:235px;width:322px">Potato Skins with Cheese &amp; Bacon<span>4.50</span></div>
  <div class="row" style="left:802px;top:258px;width:322px">Cheesy Chilli Chips<span>6.00</span></div>
  <div class="row" style="left:802px;top:287px;width:322px">Cheesy Chilli Nachos<span>6.50</span></div>
  <div class="row" style="left:802px;top:316px;width:322px">Cheesy Chips<span>4.50</span></div>
  <div class="row" style="left:802px;top:341px;width:322px">Chilli &amp; Chips<span>5.00</span></div>
  <div class="row" style="left:802px;top:374px;width:322px">Curry Sauce &amp; Chips<span>4.50</span></div>
  <div class="row" style="left:802px;top:402px;width:322px">Garlic Bread<span>3.50</span></div>
  <div class="row" style="left:802px;top:427px;width:322px">Toasted Tea-Cake with Jam<span>3.00</span></div>
  <div class="row" style="left:802px;top:460px;width:322px">Fruit Scone with Cream &amp; Jam<span>3.00</span></div>

  <!-- Sandwiches -->
  <h2 class="heading" style="left:828px;top:518px;--ul-left:40px;--ul-width:130px">Sandwiches</h2>
  <p class="note" style="left:827px;top:565px">Served with a salad garnish and homemade coleslaw</p>
  <div class="row" style="left:805px;top:589px;width:231px">Mature Cheddar Cheese<span>4.00</span></div>
  <div class="row" style="left:805px;top:611px;width:231px">Home Baked Ham<span>4.50</span></div>
  <div class="row" style="left:805px;top:632px;width:231px">Tuna Mayonnaise<span>4.50</span></div>
  <div class="row" style="left:805px;top:657px;width:231px">Chicken Mayonnaise<span>4.50</span></div>
  <div class="row" style="left:805px;top:682px;width:231px">Bacon &amp; Cheese<span>5.00</span></div>
  <div class="row" style="left:805px;top:707px;width:231px">BLT<span>5.00</span></div>
  <div class="row" style="left:805px;top:733px;width:231px">Cheese &amp; Home Baked Ham<span>5.00</span></div>
  <div class="row" style="left:805px;top:759px;width:231px">Chicken &amp; Bacon Mayonnaise<span>5.50</span></div>
  <p class="note" style="left:812px;top:780px;width:220px">Any of the above are also available as a floury soft roll or toastie</p>
  <div class="art" role="img" aria-label="Line illustration of a stacked sandwich" style="left:1042px;top:662px;width:158px;height:186px;border-radius:40% 10% 0 40%"></div>
</main>
</body>
</html>
```